NorthvaleStrategy Business Card Design

Design business cards with attached ideas. I am open to several different ideas that would be interesting and innovative. What I have provided is logo and colors. Font should be Helvetica although it could be bold or light as needed. The design can be vertical or horizontal. The design should be more interesting than a standard business card. Files must be ready to send to a printer and in Illustrator format. The text with the five icons should be exact. Send me some ideas and I will get back to you right away. I need to choose a design within 3-5 days.

Target Market(s)

Business audience

Industry/Entity Type

Business

Contact Information for Business Card

Files should be ready to send to printer in illustrator format

Font styles to use
Sans Serif

Colors
3276b5

Requirements
Must have
• Use attached logo and two colors - blue / gray
• Include 5 offering icons and text on back
Nice to have
• Interesting and innovative design. Vertical or horizontal are both fine.

```html
<!DOCTYPE html>
<html lang="en">
<head>
<meta charset="utf-8">
<title>NorthvaleStrategy Business Card</title>
<link rel="stylesheet" href="https://fonts.googleapis.com/css2?family=Open+Sans:wght@400;600;700&display=swap">
<style>
  :root {
    --backdrop: #4a423d;
    --card: #141414;
    --brand-blue: #3276b5;
    --brand-gray: #6d6e70;
    --text-light: #f2f2f2;
    --text-muted: #8a8a8a;
    --divider: #9a9a9a;
  }
  * { box-sizing: border-box; margin: 0; padding: 0; }
  html, body { width: 1200px; height: 814px; overflow: hidden; }
  body {
    background: var(--backdrop);
    font-family: "Open Sans", Helvetica, Arial, sans-serif;
    position: relative;
  }
  .card {
    position: absolute;
    width: 520px;
    height: 298px;
    background: var(--card);
    border-radius: 3px;
    box-shadow: 0 10px 24px rgba(0,0,0,.45);
    color: var(--text-light);
  }
  .card-front { left: 50px; top: 258px; }
  .card-back  { left: 630px; top: 258px; }

  /* front */
  .front-mark {
    position: absolute; left: 60px; top: 92px;
    width: 140px; text-align: center;
  }
  .mark-square {
    width: 84px; height: 84px; margin: 0 auto 10px;
    background: var(--brand-blue); border-radius: 6px;
  }
  .front-mark .brand-name {
    font-size: 12px; font-weight: 600; color: var(--text-light);
  }
  .front-divider {
    position: absolute; left: 222px; top: 86px;
    width: 1px; height: 124px; background: var(--divider);
  }
  .contact { position: absolute; left: 244px; top: 90px; }
  .contact-name {
    font-size: 20px; font-weight: 600; color: var(--brand-blue); line-height: 1.1;
  }
  .contact-title {
    font-size: 14px; color: var(--text-muted); margin-bottom: 12px;
  }
  .contact-list { list-style: none; }
  .contact-list li {
    display: flex; align-items: center; gap: 8px;
    font-size: 13.5px; line-height: 22px; color: var(--text-light);
  }
  .contact-list svg { width: 12px; height: 12px; fill: var(--text-light); flex: none; }

  /* back */
  .back-brand {
    position: absolute; left: 120px; top: 52px;
    display: flex; align-items: center; gap: 12px;
  }
  .back-brand .mark-square {
    width: 56px; height: 56px; margin: 0; background: var(--text-light); border-radius: 4px;
  }
  .back-brand .brand-name { font-size: 21px; font-weight: 700; color: var(--text-light); line-height: 1.1; }
  .back-brand .tagline { font-size: 11px; color: var(--text-light); }
  .offerings {
    position: absolute; left: 24px; right: 24px; top: 150px;
    text-align: center; font-size: 12.5px; line-height: 19px; color: var(--text-light);
  }
  .offerings .label { color: var(--brand-blue); font-weight: 600; font-size: 14px; }
  .offerings b { font-weight: 700; }
</style>
</head>
<body>
  <section class="card card-front">
    <div class="front-mark">
      <div class="mark-square"></div>
      <div class="brand-name">NorthvaleStrategy</div>
    </div>
    <div class="front-divider"></div>
    <div class="contact">
      <div class="contact-name">Daniel Hart, PhD</div>
      <div class="contact-title">Managing Director</div>
      <ul class="contact-list">
        <li><svg viewBox="0 0 24 24"><path d="M6.6 10.8a15 15 0 0 0 6.6 6.6l2.2-2.2a1 1 0 0 1 1-.25 11.4 11.4 0 0 0 3.6.57 1 1 0 0 1 1 1V20a1 1 0 0 1-1 1A17 17 0 0 1 3 4a1 1 0 0 1 1-1h3.5a1 1 0 0 1 1 1c0 1.25.2 2.45.57 3.57a1 1 0 0 1-.25 1z"/></svg>615-555-0142</li>
        <li><svg viewBox="0 0 24 24"><path d="M2 5h20v14H2z M2 5l10 8 10-8" /></svg>Daniel@NorthvaleStrategy.com</li>
        <li><svg viewBox="0 0 24 24"><circle cx="12" cy="12" r="10"/></svg>www.NorthvaleStrategy.com</li>
      </ul>
    </div>
  </section>

  <section class="card card-back">
    <div class="back-brand">
      <div class="mark-square"></div>
      <div>
        <div class="brand-name">NorthvaleStrategy</div>
        <div class="tagline">Clear Thinking · Steady Growth</div>
      </div>
    </div>
    <p class="offerings">
      <span class="label">Offerings</span> - <b>Concepts:</b> Thought leadership white papers<br>
      <b>Curriculum:</b> Short courses on strategy <b>Coaching:</b> Building your<br>
      strategic leadership <b>Consulting:</b> Developing your strategic future<br>
      <b>ScoreCard:</b> Balanced ScoreCard and software
    </p>
  </section>
</body>
</html>
```